Clean Chic Simple Black & White One sided Biz Card

I need a business card for my company Brightwater Docket Partners. We are a luxury, white glove service for organizing files for attorneys.
I would like something that is stunningly simple and chic/sexy. This is going to be only one sided. We are going to use raised ink or ink embossing for the printing. So the logo will be raised in black. I am currently waiting to hear back from the printer as to whether or not the logo has to be in all black or can be left in its current state of black with grey initials. Please check our website for inspiration. www.brightwaterdocketpartners.example.
Thank you so much for your time.

* Please decide whichever title you think looks best(Chief Executive Officer, CEO, or President)
Updates

I really like the designs that make the logo large and the main focus.  
I also like the use of modern, masculine, simple, chic fonts for the slogan and info.

1) No bold font on slogan or info
2) Shrink info to be smaller maybe to make the logo bigger and more the focus
3) Maybe use grey for all the info and slogan so the focus will be on the logo

Thank you so much for your time!!

Target Market(s)

Luxury driven lawyers and their support staff

Industry/Entity Type

Printer

Requirements
Must have
• One sided card

Modern, sleek, masculine, chic, simple font.

Please add our slogan. Refer to file labeled "old logo" to see how we added our slogan under the old logo.
The slogan is, "We Put Order to the Attorney File"

Please include the info below:
Marina Thornbury (Chief Executive Officer, CEO, or President)
812 North Delmont Avenue, Suite 1400
Los Angeles, California 90017
P: (213)555-0186 F: (213)555-0142
marinat@brightwaterdocketpartners.example
www.brightwaterdocketpartners.example

Please refer to attached file labeled "inkpressingembossing requirements" for requirements from my printer. Thank you!
Nice to have
• It can be super simple with just the logo and my info. Or it could maybe have some cool feature. Just clean please.

I would prefer the info not be in bold. I think this will help the Logo stand out as the main focus.

I attached files of how the ink pressing and embossing will look.
Should not have
• No crazy shapes and no color other than black with a white background. The logo should be the focus since it will be embossed.

```html
<!DOCTYPE html>
<html lang="en">
<head>
<meta charset="utf-8">
<title>Brightwater Docket Partners — Business Card</title>
<link href="https://fonts.googleapis.com/css2?family=Didact+Gothic&family=Cormorant+SC:wght@600&display=swap" rel="stylesheet">
<style>
  :root {
    --backdrop: #e6e4e1;
    --card: #fbfbfa;
    --ink: #151515;
    --grey: #8e8e8e;
    --mark: #a9a9a9;
    --rule: #b5b5b5;
  }
  html, body {
    margin: 0;
    width: 1200px;
    height: 1000px;
    overflow: hidden;
    background: var(--backdrop);
  }
  .stage {
    width: 1200px;
    height: 1000px;
    display: flex;
    align-items: center;
    justify-content: center;
  }
  .card {
    position: relative;
    width: 1050px;
    height: 600px;
    background: var(--card);
    box-shadow: 0 10px 30px rgba(0,0,0,0.12);
    font-family: "Didact Gothic", "Century Gothic", sans-serif;
    color: var(--ink);
  }
  .brand {
    position: absolute;
    top: 36px;
    left: 0;
    right: 0;
    display: flex;
    flex-direction: column;
    align-items: center;
  }
  .brand-dot {
    width: 96px;
    height: 96px;
    border-radius: 50%;
    background: var(--mark);
  }
  .brand-name {
    margin: 18px 0 0;
    font-family: "Cormorant SC", "Times New Roman", serif;
    font-weight: 600;
    font-size: 37px;
    letter-spacing: 5px;
    line-height: 1;
    color: var(--ink);
    white-space: nowrap;
  }
  .brand-slogan {
    margin: 10px 0 0;
    font-size: 15px;
    letter-spacing: 3px;
    color: var(--grey);
  }
  .contact {
    position: absolute;
    top: 262px;
    right: 32px;
    width: 410px;
    padding: 14px 18px;
    border: 5px solid var(--rule);
    text-align: right;
    color: var(--grey);
    font-size: 15.5px;
    line-height: 1.45;
    font-style: normal;
  }
  .contact p { margin: 0; }
  .contact .gap { display: inline-block; width: 22px; }
  .person {
    position: absolute;
    left: 48px;
    bottom: 62px;
  }
  .person-name {
    margin: 0;
    font-size: 46px;
    font-weight: 400;
    letter-spacing: 0.5px;
    color: var(--ink);
    line-height: 1;
  }
  .person-title {
    margin: 4px 0 0;
    text-align: right;
    font-size: 17px;
    color: var(--grey);
  }
</style>
</head>
<body>
<main class="stage">
  <section class="card">
    <header class="brand">
      <span class="brand-dot"></span>
      <h1 class="brand-name">BRIGHTWATER DOCKET PARTNERS, INC.</h1>
      <p class="brand-slogan">We Put Order to the Attorney File</p>
    </header>

    <address class="contact">
      <p>812 North Delmont Avenue, Suite 1400,</p>
      <p>Los Angeles, California 90017</p>
      <p>P: (213)555-0186<span class="gap"></span>F: (213)555-0142</p>
      <p>marinat@brightwaterdocketpartners.example</p>
      <p>www.brightwaterdocketpartners.example</p>
    </address>

    <div class="person">
      <h2 class="person-name">MARINA THORNBURY</h2>
      <p class="person-title">President</p>
    </div>
  </section>
</main>
</body>
</html>
```